Helix Marke Business Cards and Letterheads.
Lead Generation Specialists.
Professional
Denise Okafor
Account Manager
Wexford Court
Brindle Road
Chertsey, Surrey
RG21 4XN
UK
Denise.okafor@helixmarke.co.uk
Www.helixmarke.co.uk
In the email address please make it all lower case including the l and p in the name.
Same applies for the web address the www. Needs to all be in lower case.
We would like the background, a block colour (wash) using the blue of the text Helix Marke in our logo. We would like the logo reversed out in White together with the tag line and we would also like the inclusion of the 5 locations of our offices.
London
New York
Amsterdam
Munich
Silicon Valley

```html
<!DOCTYPE html>
<html lang="en">
<head>
<meta charset="utf-8">
<title>Helix Marke Stationery</title>
<link rel="stylesheet" href="https://fonts.googleapis.com/css2?family=Arimo:wght@400;700&display=swap">
<style>
  :root {
    --stage-dark: #111214;
    --stage-mid: #2b2d31;
    --brand-blue: #1a7fc4;
    --brand-blue-deep: #0d5a99;
    --brand-blue-light: #5fb3ea;
    --brand-orange: #f08a1c;
    --paper: #ffffff;
    --paper-shade: #f3f5f7;
    --fold-line: #d3d8de;
    --ink: #4a4f55;
    --ink-soft: #8a9099;
    --tag-grey: #b9c0c8;
  }
  * { box-sizing: border-box; margin: 0; padding: 0; }
  html, body { width: 1200px; height: 468px; overflow: hidden; }
  body {
    position: relative;
    font-family: "Arimo", Arial, sans-serif;
    background: radial-gradient(ellipse at 50% 45%, var(--stage-mid) 0%, var(--stage-dark) 80%);
    color: var(--ink);
  }
  .piece { position: absolute; }

  /* Brand lockup */
  .lockup { left: 26px; top: 52px; display: flex; align-items: flex-start; gap: 12px; }
  .lockup-dot { width: 58px; height: 58px; border-radius: 50%; background: var(--brand-blue); margin-top: 4px; }
  .lockup-name { font-size: 36px; font-weight: 700; color: var(--brand-blue); line-height: 1; }
  .lockup-tag { font-size: 14px; color: var(--tag-grey); margin-top: 5px; }
  .lockup-sub { font-size: 12px; color: var(--brand-blue-deep); margin-top: 9px; }

  /* Business cards */
  .card {
    width: 146px; height: 84px; background: var(--paper);
    border-radius: 2px; overflow: hidden;
    box-shadow: 0 2px 6px rgba(0,0,0,.5);
  }
  .card svg { position: absolute; inset: 0; }
  .card-front { top: 187px; }
  .card-front.first { left: 24px; }
  .card-front.second { left: 178px; }
  .card .brand { position: absolute; left: 8px; top: 10px; font-size: 9px; font-weight: 700; color: var(--brand-blue); }
  .card .brand-tag { position: absolute; left: 8px; top: 21px; font-size: 4px; color: var(--ink-soft); }
  .card .name { position: absolute; right: 8px; top: 8px; font-size: 7px; font-weight: 700; color: var(--brand-blue); text-align: right; }
  .card .role { position: absolute; right: 8px; top: 17px; font-size: 4.5px; color: var(--ink-soft); text-align: right; }
  .card .contact { position: absolute; right: 8px; top: 26px; font-size: 4px; line-height: 5.5px; color: var(--ink); text-align: right; }
  .card-back { top: 283px; }
  .card-back.white { left: 24px; }
  .card-back.blue { left: 178px; background: linear-gradient(135deg, var(--brand-blue-light), var(--brand-blue) 55%, var(--brand-blue-deep)); }
  .card-back .centre { position: absolute; left: 0; right: 0; text-align: center; }
  .card-back.white .centre.brand-line { top: 28px; font-size: 10px; font-weight: 700; color: var(--brand-blue); }
  .card-back.white .centre.offices { top: 60px; font-size: 4px; line-height: 6px; color: var(--ink-soft); }
  .card-back.blue .centre.brand-line { top: 24px; font-size: 11px; font-weight: 700; color: var(--paper); }
  .card-back.blue .centre.tag-line { top: 39px; font-size: 4.5px; color: var(--paper); }
  .card-back.blue .centre.web { top: 70px; font-size: 4px; color: var(--paper); }

  /* Letterhead */
  .letterhead {
    left: 437px; top: 31px; width: 194px; height: 413px;
    background: var(--paper); overflow: hidden;
    box-shadow: 0 3px 10px rgba(0,0,0,.55);
  }
  .letterhead svg { position: absolute; inset: 0; }
  .letterhead .brand { position: absolute; left: 14px; top: 20px; font-size: 11px; font-weight: 700; color: var(--brand-blue); }
  .letterhead .brand-tag { position: absolute; left: 14px; top: 33px; font-size: 4.5px; color: var(--ink-soft); }
  .letterhead .address { position: absolute; left: 110px; top: 12px; font-size: 3.6px; line-height: 6px; color: var(--ink); }

  /* Envelopes */
  .envelope { overflow: hidden; box-shadow: 0 3px 10px rgba(0,0,0,.55); }
  .envelope svg { position: absolute; inset: 0; }
  .envelope.orange-flap { left: 804px; top: 66px; width: 372px; height: 160px; background: var(--paper); }
  .envelope.plain { left: 780px; top: 162px; width: 396px; height: 160px; background: var(--paper-shade); }
  .envelope.blue-flap { left: 756px; top: 238px; width: 420px; height: 206px; background: var(--paper); }
  .envelope .flap-mark { position: absolute; left: 0; right: 0; text-align: center; font-weight: 700; color: var(--paper); font-size: 12px; }
  .envelope.orange-flap .flap-mark { top: 24px; }
  .envelope.blue-flap .flap-mark { top: 26px; }
  .envelope .brand { position: absolute; left: 22px; top: 92px; font-size: 13px; font-weight: 700; color: var(--brand-blue); }
  .envelope .brand-tag { position: absolute; left: 22px; top: 108px; font-size: 4.5px; color: var(--ink-soft); }
  .envelope .address { position: absolute; left: 22px; top: 118px; font-size: 4px; line-height: 6px; color: var(--ink); }
</style>
</head>
<body>

<header class="piece lockup">
  <div class="lockup-dot"></div>
  <div>
    <div class="lockup-name">Helix Marke</div>
    <div class="lockup-tag">Lead Generation Specialists</div>
    <div class="lockup-sub">Professional</div>
  </div>
</header>

<!-- Business card fronts -->
<article class="piece card card-front first">
  <svg width="146" height="84" viewBox="0 0 146 84">
    <path d="M0 74 C40 66 95 68 146 52 L146 84 L0 84 Z" fill="var(--brand-blue)"/>
    <path d="M0 72 C40 64 95 66 146 49" stroke="var(--brand-orange)" stroke-width="1.3" fill="none"/>
    <path d="M84 84 C100 72 120 58 146 52 L146 84 Z" fill="var(--brand-blue-deep)" opacity=".85"/>
  </svg>
  <div class="brand">Helix Marke</div>
  <div class="brand-tag">Lead Generation Specialists</div>
  <div class="name">Denise Okafor</div>
  <div class="role">Account Manager</div>
  <div class="contact">t 01932 555 014<br>denise.okafor@helixmarke.co.uk<br>www.helixmarke.co.uk</div>
</article>

<article class="piece card card-front second">
  <svg width="146" height="84" viewBox="0 0 146 84">
    <path d="M0 74 C40 66 95 68 146 52 L146 84 L0 84 Z" fill="var(--brand-blue)"/>
    <path d="M0 72 C40 64 95 66 146 49" stroke="var(--brand-orange)" stroke-width="1.3" fill="none"/>
    <path d="M84 84 C100 72 120 58 146 52 L146 84 Z" fill="var(--brand-blue-deep)" opacity=".85"/>
  </svg>
  <div class="brand">Helix Marke</div>
  <div class="brand-tag">Lead Generation Specialists</div>
  <div class="name">Denise Okafor</div>
  <div class="role">Account Manager</div>
  <div class="contact">m 07700 555 281<br>denise.okafor@helixmarke.co.uk<br>www.helixmarke.co.uk</div>
</article>

<!-- Business card backs -->
<article class="piece card card-back white">
  <div class="centre brand-line">Helix Marke</div>
  <div class="centre offices">London • New York • Amsterdam<br>Munich • Silicon Valley</div>
</article>

<article class="piece card card-back blue">
  <div class="centre brand-line">Helix Marke</div>
  <div class="centre tag-line">Lead Generation Specialists</div>
  <div class="centre web">www.helixmarke.co.uk</div>
</article>

<!-- Letterhead -->
<article class="piece letterhead">
  <svg width="194" height="413" viewBox="0 0 194 413">
    <circle cx="97" cy="185" r="52" fill="var(--brand-blue)" opacity=".07"/>
    <path d="M0 392 C60 378 120 386 194 362 L194 413 L0 413 Z" fill="var(--brand-blue)"/>
    <path d="M0 388 C60 374 120 382 194 357" stroke="var(--brand-orange)" stroke-width="1.8" fill="none"/>
    <path d="M0 400 C65 388 125 396 194 376" stroke="var(--brand-blue-light)" stroke-width="1.2" fill="none"/>
  </svg>
  <div class="brand">Helix Marke</div>
  <div class="brand-tag">Lead Generation Specialists</div>
  <div class="address">Wexford Court, Brindle Road<br>Chertsey, Surrey RG21 4XN UK<br>t 01932 555 014<br>www.helixmarke.co.uk<br>denise.okafor@helixmarke.co.uk</div>
</article>

<!-- Envelopes -->
<article class="piece envelope orange-flap">
  <svg width="372" height="160" viewBox="0 0 372 160">
    <path d="M0 0 L372 0 L186 66 Z" fill="var(--brand-orange)"/>
  </svg>
  <div class="flap-mark">Helix Marke</div>
</article>

<article class="piece envelope plain">
  <svg width="396" height="160" viewBox="0 0 396 160">
    <path d="M0 0 L198 64 L396 0" stroke="var(--fold-line)" stroke-width="1.2" fill="none"/>
  </svg>
</article>

<article class="piece envelope blue-flap">
  <svg width="420" height="206" viewBox="0 0 420 206">
    <path d="M0 0 L420 0 L210 68 Z" fill="var(--brand-blue)"/>
    <path d="M0 184 C130 170 290 178 420 148 L420 206 L0 206 Z" fill="var(--brand-blue)"/>
    <path d="M0 180 C130 166 290 174 420 143" stroke="var(--brand-orange)" stroke-width="1.8" fill="none"/>
  </svg>
  <div class="flap-mark">Helix Marke</div>
  <div class="brand">Helix Marke</div>
  <div class="brand-tag">Lead Generation Specialists</div>
  <div class="address">Wexford Court<br>Brindle Road<br>Chertsey, Surrey<br>RG21 4XN<br>UK</div>
</article>

</body>
</html>
```